Roofing contractor
Maple Ford Creek Roofing needs a postcard
Use content from attached PDF from our last flyer

Target Market(s)

people needing home improvements

Industry/Entity Type

Roofing

Requirements
Must have
• 6x9 inch - is the size of the postcard, double sided (please use the templates attached to the brief itself)
• configured for mail (ZTCM)
• Ok to use stock photography but please try to find royalty-free

```html
<!DOCTYPE html>
<html lang="en">
<head>
<meta charset="utf-8">
<title>Maple Ford Creek Roofing – Postcard</title>
<link href="https://fonts.googleapis.com/css2?family=Roboto+Condensed:ital,wght@0,300;0,400;0,700;1,400&display=swap" rel="stylesheet">
<style>
:root{
  --coral:#e8705a;
  --sky:#3f73c4;
  --sky-light:#7d9ed8;
  --charcoal:#363636;
  --white:#ffffff;
  --ink:#222222;
  --rule:#bdbdbd;
}
*{box-sizing:border-box;margin:0;padding:0}
html,body{width:1200px;height:1200px;overflow:hidden}
body{
  position:relative;
  background:linear-gradient(180deg,#dcdcdc 0%,#a9a9a9 100%);
  font-family:"Roboto Condensed",Arial,sans-serif;
  color:var(--white);
}
.abs{position:absolute}
.side-label{position:absolute;left:936px;font-weight:700;font-size:66px;color:var(--ink);letter-spacing:1px}
.card{position:absolute;left:40px;width:825px;overflow:hidden;box-shadow:0 2px 6px rgba(0,0,0,.35)}
/* FRONT */
.front{top:22px;height:557px;background:linear-gradient(180deg,var(--sky-light) 0%,var(--sky) 60%)}
.house-photo{position:absolute;left:384px;top:70px;width:441px;height:420px;
  background:linear-gradient(160deg,#8a93a3 0%,#46597f 45%,#b69e84 70%,#6b6f76 100%);
  clip-path:polygon(60% 0,100% 10%,100% 100%,0 100%,0 70%,30% 35%)}
.contact-top{position:absolute;top:28px;font-size:21px;font-weight:700;display:flex;align-items:center;gap:10px}
.logo-small{position:absolute;left:43px;top:34px;line-height:1}
.logo-small .l1{font-size:22px;font-weight:400;display:block}
.logo-small .l2{font-size:50px;font-weight:700;display:block;letter-spacing:.5px}
.offer-band-full{position:absolute;left:0;top:115px;width:536px;height:245px;background:var(--coral);
  clip-path:polygon(0 0,100% 0,68% 100%,0 100%)}
.headline{position:absolute;left:46px;color:var(--white);line-height:1}
.call-band{position:absolute;left:0;top:361px;width:400px;height:118px;background:var(--sky);
  clip-path:polygon(0 0,100% 0,98% 100%,0 100%)}
.service-bar{position:absolute;left:0;top:475px;width:825px;height:82px;background:var(--charcoal);
  clip-path:polygon(0 4%,35% 4%,55% 0,100% 4%,100% 100%,0 100%)}
.services{position:absolute;top:504px;left:44px;right:22px;display:flex;justify-content:space-between;font-size:19.5px;font-weight:700}
.services li{list-style:none;display:flex;align-items:center;gap:9px}
.services li::before{content:"";width:7px;height:7px;border-radius:50%;background:var(--coral)}
/* BACK */
.back{top:598px;height:558px;background:var(--white)}
.promo{position:absolute;left:0;top:0;width:492px;height:558px;background:var(--coral);overflow:hidden}
.promo-title{position:absolute;top:24px;left:0;width:512px;text-align:center;font-size:19.5px;font-weight:700;color:#fff;white-space:nowrap}
.tile{position:absolute;width:197px;height:94px;border:2px solid #fff}
.tile-peak{position:absolute;width:197px;height:16px}
.tile-caption{position:absolute;width:220px;text-align:center;font-size:14px;font-weight:700;color:#fff;white-space:nowrap}
.deal{position:absolute;left:26px;font-weight:700;color:#fff;line-height:1;white-space:nowrap}
.contact-bar{position:absolute;left:0;top:445px;width:492px;height:113px;background:var(--charcoal);
  clip-path:polygon(0 17%,33% 17%,46% 0,53% 0,67% 17%,100% 17%,100% 100%,0 100%)}
.contact-row{position:absolute;display:flex;align-items:center;gap:10px;white-space:nowrap}
.social{width:16px;height:16px;border-radius:50%;background:#fff}
.mail-logo{position:absolute;left:512px;top:28px;color:var(--ink);line-height:1}
.mail-logo .l1{font-size:13px;font-weight:400;display:block}
.mail-logo .l2{font-size:30px;font-weight:700;display:block}
.stamp-box{position:absolute;left:724px;top:23px;width:78px;height:78px;border:2px solid var(--ink)}
.address-line{position:absolute;left:528px;width:274px;height:1px;background:var(--rule)}
</style>
</head>
<body>

<div class="side-label" style="top:252px">FRONT</div>
<div class="side-label" style="top:836px">BACK</div>

<!-- FRONT SIDE -->
<section class="card front">
  <div class="house-photo" role="img" aria-label="Photo of a two-storey house with grey shingle roof, blue siding and stone gable"></div>

  <div class="logo-small"><span class="l1">MAPLE FORD CREEK</span><span class="l2">ROOFING</span></div>

  <div class="contact-top" style="left:285px">
    <svg width="24" height="16" viewBox="0 0 24 16"><rect x="1" y="1" width="22" height="14" fill="none" stroke="#fff" stroke-width="2"/><path d="M1 1l11 8 11-8" fill="none" stroke="#fff" stroke-width="2"/></svg>
    hello@mfcroofing.com
  </div>
  <div class="contact-top" style="left:595px">
    <svg width="18" height="18" viewBox="0 0 18 18" fill="none" stroke="#fff" stroke-width="1.5"><circle cx="9" cy="9" r="8"/><ellipse cx="9" cy="9" rx="3.5" ry="8"/><path d="M1 9h16M2.5 5h13M2.5 13h13"/></svg>
    www.mfcroofing.com
  </div>

  <div class="offer-band-full"></div>
  <div class="headline" style="top:130px;font-size:32px;font-weight:400">CONSIDERING A NEW ROOF</div>
  <div class="headline" style="top:180px;font-size:38px;font-weight:700">MAPLE FORD CREEK</div>
  <div class="headline" style="top:228px;font-size:29px;font-weight:700">ROOFING &amp; SHEET METAL</div>
  <div class="abs" style="left:46px;top:274px;width:360px;height:1px;background:rgba(255,255,255,.5)"></div>
  <div class="headline" style="top:292px;font-size:15px;font-style:italic;line-height:1.3">WE'VE BEEN BUILDING TRUST AND SERVING OUR<br>CUSTOMERS IN THE MAPLE FORD CREEK AREA WITH</div>
  <div class="headline" style="top:334px;font-size:22px;font-weight:700">WITH INTEGRITY SINCE 1995</div>

  <div class="call-band"></div>
  <svg class="abs" style="left:45px;top:386px" width="22" height="22" viewBox="0 0 24 24" fill="none" stroke="#fff" stroke-width="2"><path d="M6 3l3 4-2 2c1 3 3 5 6 6l2-2 4 3-2 4C9 20 4 15 2 7z"/></svg>
  <div class="headline" style="left:85px;top:376px;font-size:40px;font-weight:700">555-018-2373</div>
  <div class="headline" style="left:85px;top:422px;font-size:23px;font-weight:300;line-height:1.2">To make an appointment<br>or ask questions</div>

  <div class="service-bar"></div>
  <ul class="services">
    <li>Roof Repair</li><li>Skylight Replacement</li><li>Chimney Caps &amp; Repair</li><li>Roof Maintenance</li>
  </ul>
</section>

<!-- BACK SIDE -->
<section class="card back">
  <div class="promo">
    <div class="promo-title" style="width:492px">TAKE ADVANTAGE OF OUR 2018 PROMOTIONS</div>

    <svg class="tile-peak" style="left:27px;top:56px" viewBox="0 0 197 16" preserveAspectRatio="none"><polygon points="0,16 98,0 197,16" fill="#4b4b4b"/></svg>
    <div class="tile" style="left:27px;top:71px;background:linear-gradient(180deg,#5a5c5c,#3e4040)" role="img" aria-label="Close-up of architectural shingles"></div>
    <div class="tile-caption" style="left:16px;top:175px">50 YR ARCHITECTURAL SHINGLES</div>

    <svg class="tile-peak" style="left:261px;top:56px" viewBox="0 0 197 16" preserveAspectRatio="none"><polygon points="0,16 98,0 197,16" fill="#3f73c4"/></svg>
    <div class="tile" style="left:261px;top:71px;background:linear-gradient(180deg,#3a7a62 0%,#3a7a62 48%,#eef0ee 50%,#cfd4d2 100%)" role="img" aria-label="Building with green standing-seam metal roof"></div>
    <div class="tile-caption" style="left:250px;top:175px">PREMIUM METAL ROOFING</div>

    <svg class="tile-peak" style="left:27px;top:224px" viewBox="0 0 197 16" preserveAspectRatio="none"><polygon points="0,16 98,0 197,16" fill="#a9c6e6"/></svg>
    <div class="tile" style="left:27px;top:239px;background:linear-gradient(160deg,#a9c6e6 0%,#a48e7c 45%,#e7dccd 75%,#8f7f70 100%)" role="img" aria-label="Roof edge with gutter and downspout"></div>
    <div class="tile-caption" style="left:16px;top:343px">GUTTER &amp; DOWNSPOUT</div>

    <svg class="tile-peak" style="left:261px;top:224px" viewBox="0 0 197 16" preserveAspectRatio="none"><polygon points="0,16 98,0 197,16" fill="#555"/></svg>
    <div class="tile" style="left:261px;top:239px;background:linear-gradient(170deg,#5a5a5a 0%,#c9cccd 35%,#9ea2a4 100%)" role="img" aria-label="Perforated metal gutter guard on a roof edge"></div>
    <div class="tile-caption" style="left:250px;top:343px">GUTTER GUARD</div>

    <div class="deal" style="top:374px;font-size:23px;font-weight:400"><b>5% to 25% OFF</b> SELECT SERVICES NOW</div>
    <div class="deal" style="top:403px;font-size:32px">THROUGH DECEMBER 31, 2018</div>

    <div class="contact-bar"></div>
    <div class="contact-row" style="left:26px;top:482px;font-size:27px;font-weight:700">
      <svg width="18" height="18" viewBox="0 0 24 24" fill="none" stroke="#fff" stroke-width="2"><path d="M6 3l3 4-2 2c1 3 3 5 6 6l2-2 4 3-2 4C9 20 4 15 2 7z"/></svg>
      555-018-2373
    </div>
    <div class="contact-row" style="left:26px;top:516px;font-size:16px">
      <svg width="16" height="16" viewBox="0 0 18 18" fill="none" stroke="#fff" stroke-width="1.5"><circle cx="9" cy="9" r="8"/><ellipse cx="9" cy="9" rx="3.5" ry="8"/><path d="M1 9h16"/></svg>
      www.mfcroofing.com
    </div>
    <div class="contact-row" style="left:258px;top:487px;font-size:15px">
      <svg width="16" height="11" viewBox="0 0 24 16"><rect x="1" y="1" width="22" height="14" fill="none" stroke="#fff" stroke-width="2"/><path d="M1 1l11 8 11-8" fill="none" stroke="#fff" stroke-width="2"/></svg>
      hello@mfcroofing.com
    </div>
    <div class="contact-row" style="left:260px;top:517px;gap:20px">
      <span class="social"></span><span class="social"></span><span class="social"></span>
    </div>
  </div>

  <div class="mail-logo"><span class="l1">MAPLE FORD CREEK</span><span class="l2">ROOFING</span></div>
  <div class="stamp-box"></div>
  <div class="address-line" style="top:280px"></div>
  <div class="address-line" style="top:318px"></div>
  <div class="address-line" style="top:356px"></div>
  <div class="address-line" style="top:394px"></div>
</section>

</body>
</html>
```